Design some Business Cards for Quiet Heron Design

I need a business card developed for my business Quiet Heron Design [login to view URL]
We are an alpine and snow sport inspired graphic apparel company (T shirts, hoodies, beanies etc). Check out our website for color schemes. I have attached source files for both the company logo and the Heron's head. It might be nice to have a faint watermark of the Heron head somehow on one side of the card with the contact information and the logo could be on the other side. I have attached both the Heron head for dark backgrounds as well as light colored backgrounds.
Our tag line is "Chase The Ridgelineā„¢" and needs to be on the same side with the logo and perhaps "Alpine and Snow Sport Inspired Graphic Apparel" as well

My Contact information for the card is
Corbin Hale
owner
519-847-3062
and of course the web site [login to view URL] where you think it would work well.

Good luck

```html
<!DOCTYPE html>
<html lang="en">
<head>
<meta charset="utf-8">
<title>Quiet Heron Design — Business Cards</title>
<link href="https://fonts.googleapis.com/css2?family=Roboto:wght@400;500;700;900&display=swap" rel="stylesheet">
<style>
  :root {
    --bg: #2b2b2d;
    --card-white: #ffffff;
    --brand-orange: #e8472a;
    --brand-orange-deep: #d03c21;
    --brand-blue: #2b6cb3;
    --ink-grey: #5a5a5a;
    --faint-grey: #ececec;
    --panel-shadow: rgba(0,0,0,0.08);
  }
  * { margin: 0; padding: 0; box-sizing: border-box; }
  html, body {
    width: 1200px; height: 1023px; overflow: hidden;
    background: var(--bg);
    font-family: "Roboto", Arial, sans-serif;
  }
  .sheet {
    position: relative; width: 1200px; height: 1023px;
    display: flex; align-items: center; justify-content: center; gap: 40px;
  }
  .card {
    position: relative; width: 540px; height: 309px; overflow: hidden;
    box-shadow: 0 10px 30px rgba(0,0,0,0.45);
  }

  /* Front: contact side */
  .card--front { background: var(--card-white); }
  .card--front .watermark {
    position: absolute; left: 40px; top: 40px; width: 210px; height: 220px;
    border-radius: 46% 46% 40% 40%;
    background: radial-gradient(ellipse at 50% 40%, #f1f1f1 0%, #f6f6f6 60%, rgba(255,255,255,0) 100%);
  }
  .card--front .brand {
    position: absolute; left: 38px; top: 140px;
  }
  .brand-name {
    font-weight: 900; font-size: 25px; letter-spacing: -0.3px; line-height: 1;
    color: var(--brand-orange);
  }
  .brand-tagline {
    margin-top: 6px; font-weight: 500; font-size: 14px; color: var(--ink-grey);
  }
  .info-panel {
    position: absolute; left: 292px; top: 0; right: 0; bottom: 14px;
    padding: 28px 0 0 30px;
    border-left: 1px solid var(--faint-grey);
    box-shadow: -6px 0 10px -6px var(--panel-shadow);
  }
  .contact-name {
    font-weight: 700; font-size: 15px; letter-spacing: 0.5px; text-transform: uppercase;
    color: var(--brand-orange);
  }
  .contact-role { font-size: 13px; color: var(--ink-grey); margin-bottom: 14px; }
  .contact-row { display: flex; gap: 10px; margin-bottom: 10px; align-items: flex-start; }
  .contact-row svg { width: 15px; height: 15px; margin-top: 3px; flex: none; }
  .contact-label { font-weight: 700; font-size: 12px; color: var(--brand-blue); line-height: 1.2; }
  .contact-value { font-size: 12px; color: var(--ink-grey); line-height: 1.3; }
  .edge-band { position: absolute; left: 0; right: 0; bottom: 0; height: 14px; }

  /* Back: brand side */
  .card--back { background: var(--brand-orange); }
  .card--back .watermark {
    position: absolute; left: 150px; top: 24px; width: 240px; height: 240px;
    border-radius: 46% 46% 40% 40%;
    background: radial-gradient(ellipse at 50% 40%, var(--brand-orange-deep) 0%, #dc4125 55%, rgba(232,71,42,0) 100%);
  }
  .card--back .brand {
    position: absolute; left: 0; right: 0; top: 128px; text-align: center;
  }
  .card--back .brand-name { color: #ffffff; font-size: 30px; }
  .card--back .brand-tagline { color: #ffffff; font-size: 15px; }
  .back-web {
    position: absolute; right: 34px; bottom: 26px;
    font-weight: 700; font-size: 14px; color: #ffffff;
  }
</style>
</head>
<body>
<main class="sheet">

  <section class="card card--front" aria-label="Business card front">
    <div class="watermark" role="img" aria-label="Faint heron head illustration watermark"></div>
    <div class="brand">
      <div class="brand-name">Quiet Heron Design</div>
      <div class="brand-tagline">Chase The Ridgeline™</div>
    </div>

    <div class="info-panel">
      <div class="contact-name">Corbin Hale</div>
      <div class="contact-role">Owner</div>

      <div class="contact-row">
        <svg viewBox="0 0 16 16" aria-hidden="true"><path d="M4 1.5l2.5 3-1.5 1.8c.8 1.8 2 3 3.8 3.8l1.7-1.5 3 2.5-1.5 2.4C7 13.5 2.5 9 1.5 3z" fill="#555"/></svg>
        <div><div class="contact-label">Phone</div><div class="contact-value">519-847-3062</div></div>
      </div>
      <div class="contact-row">
        <svg viewBox="0 0 16 16" aria-hidden="true"><circle cx="8" cy="8" r="6.5" fill="none" stroke="#555" stroke-width="1.6"/><path d="M1.5 8h13M8 1.5c-3 3.5-3 9.5 0 13M8 1.5c3 3.5 3 9.5 0 13" fill="none" stroke="#555" stroke-width="1.2"/></svg>
        <div><div class="contact-label">Web</div><div class="contact-value">www.quietheron.ca</div></div>
      </div>
      <div class="contact-row">
        <svg viewBox="0 0 16 16" aria-hidden="true"><rect x="1.5" y="3.5" width="13" height="9" fill="none" stroke="#555" stroke-width="1.4"/><path d="M1.5 3.5L8 9l6.5-5.5" fill="none" stroke="#555" stroke-width="1.4"/></svg>
        <div><div class="contact-label">Email</div><div class="contact-value">info@quietheron.ca</div></div>
      </div>
    </div>

    <svg class="edge-band" viewBox="0 0 540 14" preserveAspectRatio="none" aria-hidden="true">
      <polygon points="0,0 290,0 302,14 0,14" fill="var(--brand-blue)"/>
      <polygon points="290,0 540,0 540,14 302,14" fill="var(--brand-orange)"/>
    </svg>
  </section>

  <section class="card card--back" aria-label="Business card back">
    <div class="watermark" role="img" aria-label="Heron head illustration in darker orange"></div>
    <div class="brand">
      <div class="brand-name">Quiet Heron Design</div>
      <div class="brand-tagline">Chase The Ridgeline™</div>
    </div>
    <div class="back-web">www.quietheron.ca</div>
  </section>

</main>
</body>
</html>
```